Brenmoor Group needs a business card

I would like the card to be simple but modern and elegant.
I like black and white.
or black and gold.
we are a private finance lender and also are involved in property and property developments.

please look at the business card photos i provided i would like B.G only one one side and all the other details on the other side use fonts that tie in with my theme.

Industry/Entity Type

Finance

Contact Information for Business Card

Brenmoor Group (B.G) Callum Brenmoor M: 0418396152 E: callumbren@quivomail.com

Font styles to use
Other font styles liked:
• Use fonts that would reflect our business

Colors
000000
ffffff

Requirements
Must have
• one side of details
• other side has either B.G or Brenmoor Group like in the photos provided

```html
<!DOCTYPE html>
<html lang="en">
<head>
<meta charset="UTF-8">
<title>Brenmoor Group — Business Card</title>
<link rel="stylesheet" href="https://fonts.googleapis.com/css2?family=Playfair+Display:wght@400&family=Great+Vibes&display=swap">
<style>
  :root {
    --paper: #ffffff;
    --card: #000000;
    --gold: #d2b925;
    --gold-dim: #756614;
  }
  * { margin: 0; padding: 0; box-sizing: border-box; }
  html, body {
    width: 927px;
    height: 1200px;
    overflow: hidden;
    background: var(--paper);
  }
  .sheet {
    position: relative;
    width: 927px;
    height: 1200px;
  }
  .card {
    position: absolute;
    left: 56px;
    width: 816px;
    height: 465px;
    background: var(--card);
    color: var(--gold);
  }
  .card--front { top: 40px; }
  .card--back { top: 715px; }

  .frame-outer, .frame-inner {
    position: absolute;
    border: 2px solid var(--gold);
  }
  .frame-outer { inset: 14px; }
  .frame-inner { inset: 19px; border-width: 1.5px; }

  .name-panel {
    position: absolute;
    left: 99px;
    top: 70px;
    width: 619px;
    height: 326px;
    border: 2px solid var(--gold-dim);
    display: flex;
    align-items: center;
    justify-content: center;
  }
  .brand-name {
    font-family: "Playfair Display", "Didot", serif;
    font-weight: 400;
    font-size: 66px;
    line-height: 1;
    white-space: nowrap;
  }

  .company-name {
    position: absolute;
    left: 0; right: 0;
    top: 44px;
    text-align: center;
    font-family: "Great Vibes", cursive;
    font-weight: 400;
    font-size: 62px;
    line-height: 1.2;
    white-space: nowrap;
  }
  .rule {
    position: absolute;
    left: 38px;
    right: 38px;
    height: 2px;
    background: var(--gold);
  }
  .rule--top { top: 137px; }
  .rule--bottom { top: 353px; }

  .contact {
    position: absolute;
    left: 0; right: 0;
    top: 156px;
    text-align: center;
    font-family: "Great Vibes", cursive;
    font-weight: 400;
    font-size: 32px;
    line-height: 63px;
    list-style: none;
  }
  .currency-mark {
    position: absolute;
    left: 0; right: 0;
    top: 372px;
    text-align: center;
    font-family: "Playfair Display", serif;
    font-weight: 400;
    font-size: 56px;
    line-height: 1;
  }
</style>
</head>
<body>
<main class="sheet">
  <section class="card card--front" aria-label="Card front">
    <div class="frame-outer"></div>
    <div class="frame-inner"></div>
    <div class="name-panel">
      <p class="brand-name">Brenmoor Group</p>
    </div>
  </section>

  <section class="card card--back" aria-label="Card back">
    <div class="frame-outer"></div>
    <div class="frame-inner"></div>
    <p class="company-name">Brenmoor Group (B.G)</p>
    <div class="rule rule--top"></div>
    <ul class="contact">
      <li class="contact__name">Callum Brenmoor</li>
      <li class="contact__phone">M: 0418396152</li>
      <li class="contact__email">E: callumbren@quivomail.com</li>
    </ul>
    <div class="rule rule--bottom"></div>
    <div class="currency-mark">$</div>
  </section>
</main>
</body>
</html>
```